Quillmoor Properties, LLC. What we do is rehab homes for the purpose of flipping them and also have a rental portfolio as well.

We do not have a logo so that will need to be part of the design process

Would like, if possible to have a house or something with housing or remodeling incorporated in design.

Rental

Dale Wemberton
514 fenwick Ct.
Harlow Grove, il 60199
847-555-0142
Fax 630-555-0187

```html
<!DOCTYPE html>
<html lang="en">
<head>
<meta charset="utf-8">
<title>Quillmoor Properties, LLC — Business Card</title>
<link rel="stylesheet" href="https://fonts.googleapis.com/css2?family=Russo+One&family=Nunito+Sans:wght@800&family=Didact+Gothic&display=swap">
<style>
  :root {
    --page: #ffffff;
    --navy: #1f2c4b;
    --gold: #d9b233;
    --white: #ffffff;
  }
  html, body {
    margin: 0;
    padding: 0;
    width: 1200px;
    height: 867px;
    overflow: hidden;
    background: var(--page);
  }
  .canvas {
    position: relative;
    width: 1200px;
    height: 867px;
  }
  .card {
    position: absolute;
    left: 125px;
    top: 142px;
    width: 920px;
    height: 577px;
    background: var(--navy);
    border-radius: 40px;
    overflow: hidden;
  }
  .brand-mark {
    position: absolute;
    left: 411px;
    top: 120px;
    width: 68px;
    height: 68px;
    background: var(--gold);
  }
  .rule {
    position: absolute;
    left: 0;
    top: 226px;
    width: 100%;
    height: 6px;
    background: var(--gold);
  }
  .company-name {
    position: absolute;
    left: 0;
    top: 252px;
    width: 876px;
    margin: 0;
    text-align: center;
    font-family: "Russo One", sans-serif;
    font-size: 29px;
    font-weight: 400;
    letter-spacing: 0.3px;
    text-transform: uppercase;
    color: var(--gold);
  }
  .contact {
    position: absolute;
    left: 0;
    top: 332px;
    width: 876px;
    text-align: center;
    color: var(--white);
  }
  .person-name {
    margin: 0 0 14px;
    font-family: "Nunito Sans", sans-serif;
    font-weight: 800;
    font-size: 35px;
    line-height: 52px;
  }
  .contact-line {
    margin: 0;
    font-family: "Didact Gothic", sans-serif;
    font-size: 30px;
    line-height: 48px;
    display: flex;
    justify-content: center;
    align-items: center;
    gap: 6px;
  }
  .contact-line svg {
    width: 26px;
    height: 28px;
    flex: none;
  }
  .address {
    margin-top: 4px;
  }
</style>
</head>
<body>
<div class="canvas">
  <div class="card">
    <div class="brand-mark" aria-hidden="true"></div>
    <div class="rule"></div>
    <p class="company-name">Quillmoor Properties, LLC</p>
    <div class="contact">
      <p class="person-name">Dale Wemberton</p>
      <p class="contact-line">
        <svg viewBox="0 0 26 28" aria-label="Mobile">
          <rect x="6" y="3" width="14" height="22" rx="2" fill="none" stroke="#ffffff" stroke-width="2"/>
          <line x1="11" y1="21" x2="15" y2="21" stroke="#ffffff" stroke-width="1.6"/>
        </svg>
        <span>847-555-0142</span>
      </p>
      <p class="contact-line">
        <svg viewBox="0 0 26 28" aria-label="Fax">
          <rect x="7" y="3" width="12" height="8" fill="none" stroke="#ffffff" stroke-width="1.8"/>
          <rect x="2" y="11" width="22" height="11" rx="2" fill="none" stroke="#ffffff" stroke-width="1.8"/>
          <rect x="5" y="17" width="16" height="8" fill="#ffffff"/>
          <line x1="5" y1="14" x2="10" y2="14" stroke="#ffffff" stroke-width="1.6"/>
        </svg>
        <span>630-555-0187</span>
      </p>
      <p class="contact-line address">514 fenwick Ct. Harlow Grove, il 60199</p>
    </div>
  </div>
</div>
</body>
</html>
```